Business Card Design for an Investment Company

We need a business card design for our private investment company, called Ashbourne Partners. Ashbourne Partners is an investments partnership that aims to acquire shares in listed companies with a view to influencing those companies through active dialogue in order to improve their value. We need designs that use the logo colors (blue, grey, white), we need both English and Arabic on the business cards (can be on one side or 2 sides). The final logo should communicate professionalism, conservatism (nothing too fancy or too cheesy), that we are smart, conservative and old school.

Target Market(s)

Investment companies

Industry/Entity Type

Investment

Contact Information for Business Card

Khalid Yousef Rumaithi
Senior Executive Officer

Palm Terrace 07, Level 3, Office 215/12
HLMZ

+9714987650
krumaithi@ashbournepartners.com
www.ashbournepartners.com

Requirements
Must have
• Logo to be placed on the left hand side of the business card
• for the Arabic, we only need to have the name and title so it can be accomodated on one side so we can have the other side with full color and logo. The arabic that needs to be used is the below:
• خالد يوسف الرميثي
• المدير التنفيدي

```html
<!DOCTYPE html>
<html lang="en">
<head>
<meta charset="utf-8">
<title>Ashbourne Partners – Business Card</title>
<link rel="stylesheet" href="https://fonts.googleapis.com/css2?family=Lato:wght@400;700;900&family=Noto+Naskh+Arabic:wght@400&display=swap">
<style>
  :root {
    --brand-blue: #0a6ea3;
    --brand-grey: #555759;
    --text-grey: #6a6b6d;
    --card-white: #ffffff;
    --backdrop: #d9d8d9;
  }
  * { margin: 0; padding: 0; box-sizing: border-box; }
  html, body {
    width: 1200px; height: 807px; overflow: hidden;
    background: var(--backdrop);
    font-family: "Lato", sans-serif;
  }
  .stage {
    position: relative; width: 1200px; height: 807px;
    display: flex; align-items: center; justify-content: center; gap: 50px;
  }
  .card {
    position: relative; width: 500px; height: 286px;
    box-shadow: 0 6px 18px rgba(0,0,0,0.18);
  }
  .card--front { background: var(--card-white); }
  .card--back {
    background: var(--brand-blue);
    display: flex; align-items: center; justify-content: center;
  }
  .wordmark {
    display: flex; align-items: center; gap: 8px;
    font-weight: 900; letter-spacing: -0.5px;
  }
  .wordmark__square { width: 14px; height: 14px; flex: none; }
  .card--front .wordmark {
    position: absolute; left: 34px; top: 40px;
    font-size: 28px; color: var(--brand-blue);
  }
  .card--front .wordmark__square { background: var(--brand-grey); }
  .card--back .wordmark { font-size: 34px; color: var(--card-white); }
  .card--back .wordmark__square { background: var(--card-white); width: 16px; height: 16px; }

  .arabic {
    position: absolute; right: 30px; top: 36px;
    font-family: "Noto Naskh Arabic", serif; direction: rtl; text-align: right;
    color: var(--brand-blue); font-size: 12px; line-height: 1.6;
  }
  .details { position: absolute; left: 34px; top: 112px; color: var(--text-grey); }
  .details__name { font-weight: 700; font-size: 16px; color: var(--brand-grey); }
  .details__title { font-weight: 700; font-size: 12.5px; color: var(--brand-blue); margin-top: 2px; }
  .details__address { font-size: 12.5px; line-height: 1.4; margin-top: 8px; }
  .contacts { list-style: none; margin-top: 8px; font-size: 12.5px; }
  .contacts li { display: flex; align-items: center; gap: 9px; line-height: 1.55; }
  .contacts svg { width: 11px; height: 11px; flex: none; }
</style>
</head>
<body>
<main class="stage">
  <section class="card card--front" aria-label="Business card front">
    <div class="wordmark"><span class="wordmark__square"></span>Ashbourne Partners</div>
    <div class="arabic">
      <p>خالد يوسف الرميثي</p>
      <p>المدير التنفيدي</p>
    </div>
    <div class="details">
      <p class="details__name">Khalid Yousef Rumaithi</p>
      <p class="details__title">Senior Executive Officer</p>
      <p class="details__address">Palm Terrace 07, Level 3,<br>Office 215/12, HLMZ</p>
      <ul class="contacts">
        <li>
          <svg viewBox="0 0 12 12" aria-hidden="true"><circle cx="6" cy="6" r="6" fill="var(--brand-blue)"/><path d="M4 3.2c.4-.3.8-.2 1 .2l.4.8c.1.3 0 .5-.2.7l-.3.2c.3.7.8 1.2 1.5 1.5l.2-.3c.2-.2.4-.3.7-.2l.8.4c.4.2.5.6.2 1l-.4.4c-1.9.3-4.3-2.1-4-4z" fill="#fff"/></svg>
          +9714987650
        </li>
        <li>
          <svg viewBox="0 0 12 12" aria-hidden="true"><rect width="12" height="12" rx="2" fill="var(--brand-blue)"/><rect x="2.5" y="3.5" width="7" height="5" fill="none" stroke="#fff" stroke-width="0.9"/><path d="M2.5 3.5 6 6.3 9.5 3.5" fill="none" stroke="#fff" stroke-width="0.9"/></svg>
          krumaithi@ashbournepartners.com
        </li>
        <li>
          <svg viewBox="0 0 12 12" aria-hidden="true"><circle cx="6" cy="6" r="6" fill="var(--brand-blue)"/><circle cx="6" cy="6" r="3.6" fill="none" stroke="#fff" stroke-width="0.8"/><ellipse cx="6" cy="6" rx="1.5" ry="3.6" fill="none" stroke="#fff" stroke-width="0.8"/><path d="M2.4 6h7.2" stroke="#fff" stroke-width="0.8"/></svg>
          www.ashbournepartners.com
        </li>
      </ul>
    </div>
  </section>

  <section class="card card--back" aria-label="Business card back">
    <div class="wordmark"><span class="wordmark__square"></span>Ashbourne Partners</div>
  </section>
</main>
</body>
</html>
```